Integrated Health Clinic brochure

We need a brochure designed to highlight the services that we offer at the integrated clinic. Please see "Our Services" of our website for description of services to be added to the brochure except for Acupuncture, which is described below:

"Acupuncture is an ancient Chinese methodology that has been proven to be very effective in many health issues, particularly in relieving pain. It involves the stimulation of acupuncture points on the body to regain the natural balance of the body. Medical Acupuncture is effective in treating a wide variety of conditions including: headaches, neck and back pains, carpal tunnel syndrome, fibromyalgia, asthma, allergies, sinus problems, digestive disorders and many others."

our motto "Relieve, Rejuvenate, Renew"

Services we provide:
Chiropractic
Physiotherapy
Family counselling
Massage Therapy
Acupuncture
Osteopath

Colors are blue and green.

See our website www.velmorahealth.ca

```html
<!DOCTYPE html>
<html lang="en">
<head>
<meta charset="utf-8">
<title>Velmora Health &amp; Care Brochure</title>
<link href="https://fonts.googleapis.com/css2?family=Arimo:wght@400;700&family=Open+Sans:wght@300;400;600&display=swap" rel="stylesheet">
<style>
:root{
  --frame:#8f9092;
  --panel-light:#ebebec;
  --blue:#1f7cc2;
  --blue-soft:#3a8fd0;
  --green:#8dc540;
  --teal-top:#6fbccb;
  --teal-bottom:#b6dde6;
  --ink:#555759;
  --dark:#2b2b2b;
  --white:#ffffff;
}
*{margin:0;padding:0;box-sizing:border-box}
html,body{width:780px;height:1200px;overflow:hidden}
body{background:var(--frame);font-family:"Arimo",Arial,sans-serif;position:relative}
.abs{position:absolute}

/* outside spread */
.team-panel{left:19px;top:19px;width:495px;height:336px;background:var(--panel-light)}
.team{left:25px;top:36px;width:210px}
.team h2{color:var(--blue);font-size:12.5px;font-weight:700;margin-bottom:10px}
.member{margin-bottom:9px;line-height:1.15}
.member b{display:block;color:var(--blue);font-size:9.5px}
.member span{display:block;color:var(--blue-soft);font-size:9.5px}
.motto{left:235px;top:35px;width:240px;text-align:center;color:var(--ink);font-size:9.5px;line-height:1.15}
.motto h3{color:var(--blue);font-size:11px;font-weight:700;margin-top:10px}
.motto h3:first-child{margin-top:0}
.hero-photo{left:514px;top:19px;width:250px;height:336px;
  background:linear-gradient(160deg,#9ccbe6 0%,#c8e0ee 18%,#7aa84a 28%,#c98a62 45%,#e7b89b 60%,#b77a5c 72%,#d75c6a 85%,#8fb45a 100%)}
.dark-strip{left:19px;top:353px;width:745px;height:19px;background:linear-gradient(90deg,#3a3a3a,#5a5a5a 50%,#3a3a3a)}
.mission{left:19px;top:372px;width:247px;height:220px;background:var(--blue);color:var(--white);
  font-size:11px;font-weight:700;line-height:1.3;padding:20px 22px}
.contact{left:266px;top:372px;width:248px;height:220px;background:var(--green);color:var(--white);
  font-family:"Open Sans",Arial,sans-serif;font-size:11.5px;padding:18px 27px;line-height:1.3}
.contact p{margin-bottom:13px}
.social{display:flex;align-items:center;gap:5px;font-size:7.5px;margin-bottom:6px}
.social i{width:8px;height:8px;border-radius:50%;background:var(--white);display:block}
.map{left:291px;top:517px;width:197px;height:59px;background:linear-gradient(135deg,#e6e3dc,#cfd6c9);border:3px solid #4d4d4d}
.brand-panel{left:514px;top:372px;width:250px;height:220px;background:var(--white)}
.brand{left:566px;top:468px;display:flex;align-items:center;gap:6px}
.brand i{width:30px;height:30px;background:var(--green);display:block}
.brand span{font-size:26px;color:var(--blue);font-weight:700;font-family:"Arimo",Arial,sans-serif}

/* inside spread */
.inside{left:19px;top:607px;width:745px;height:577px;background:linear-gradient(180deg,#e9eaeb,#f7f7f7 40%,#e5e6e7)}
.services-band{left:19px;top:607px;width:745px;height:45px;background:linear-gradient(90deg,#1e1e1e,#7b7b7b 12%,#3a3a3a 28%,#3a3a3a 72%,#7b7b7b 88%,#1e1e1e)}
.services-tab{left:266px;top:607px;width:248px;height:47px;background:#111;border-radius:0 0 10px 10px;
  color:#6f6f6f;font-family:"Open Sans",Arial,sans-serif;font-weight:300;font-size:21px;text-align:center;line-height:47px}
.services-tab b{font-weight:400;color:#8a8a8a}
.service-title{height:24px;background:var(--green);color:var(--white);border-radius:5px 5px 0 0;
  font-family:"Open Sans",Arial,sans-serif;font-size:11px;text-align:center;line-height:24px;width:150px}
.card{width:197px;border-radius:8px;background:linear-gradient(180deg,var(--teal-top),var(--teal-bottom) 60%,#d5ecf1);overflow:hidden}
.card p{color:var(--white);font-size:6.6px;line-height:1.25;padding:10px 15px 0;text-align:justify}
.card ul{color:var(--white);font-size:6.6px;line-height:1.25;padding:0 15px 0 26px}
.card-photo{position:absolute;left:0;right:0;bottom:0}
</style>
</head>
<body>

<section class="abs team-panel"></section>
<div class="abs team">
  <h2>OUR TEAM</h2>
  <div class="member"><b>Dr. Owen Hartley B.A., D.C.</b><span>Chiropractor, Active Tissue Release (ATR) Provider</span></div>
  <div class="member"><b>Dr. Renata Vale, D.C.</b><span>Chiropractor and Contemporary Medical Acupuncturist</span></div>
  <div class="member"><b>Mr. Daniel Porter, MSW, RSW</b><span>Registered Social Worker</span></div>
  <div class="member"><b>Ms. Clara Brenholt</b><span>Registered Massage Therapist</span></div>
  <div class="member"><b>Ms. Irene Soong, DO(MP)</b><span>Osteopath &amp; Certified Acupuncturist</span></div>
  <div class="member"><b>Ms. Grace (Mei Lin) Ho</b><span>Certified Acupuncturist</span></div>
  <div class="member"><b>Ms. Priya Rao</b><span>Physiotherapist</span></div>
</div>
<div class="abs motto">
  <h3>RELIEVE</h3><p>Pain is not a normal part of life.</p>
  <h3>REJUVENATE</h3><p>Relieve stress. Improve performance.</p>
  <h3>RENEW</h3><p>Stressed out? Always tired? Lack of<br>energy?<br>We help recuperate and maximize your<br>performance.</p>
</div>
<div class="abs hero-photo" role="img" aria-label="Photo collage: person cartwheeling on grass, woman receiving a massage, woman stretching outdoors"></div>
<div class="abs dark-strip"></div>

<section class="abs mission">At Velmora, we believe HEALTH starts with CARE. We take a genuine interest in the wellbeing of our clients and take an integrated approach to health, ensuring you are at your optimal best physically and emotionally.</section>
<section class="abs contact">
  <p>1480 Marlow Avenue, Suite 310,<br>Toronto, Ontario</p>
  <p>1-800-555-0147</p>
  <p>www.velmorahealth.ca</p>
  <div class="social"><i></i>Velmora-Health-Wellness</div>
  <div class="social"><i></i>@VelmoraHealth</div>
</section>
<div class="abs map" role="img" aria-label="Street map showing the clinic location"></div>
<section class="abs brand-panel"></section>
<div class="abs brand"><i></i><span>Velmora</span></div>

<section class="abs inside"></section>
<div class="abs services-band"></div>
<div class="abs services-tab">OUR <b>SERVICES</b></div>

<!-- row 1 -->
<div class="abs service-title" style="left:67px;top:671px">CHIROPRACTIC</div>
<article class="abs card" style="left:43px;top:695px;height:221px">
  <p>Chiropractic care is a safe, non-invasive, drug-free therapy to correct and prevent joint and muscle pain. By restoring the natural alignment in your body, chiropractic treatments restore movement and prevent potential injuries. Chiropractic treatments are especially effective in treating back, neck, pelvis and joint problems. Procedures most often used are adjustments or spinal manipulative therapy. Adjustments are safe, painless manual procedures where our skilled chiropractors manually apply pressures to your body to restore the natural alignment. Other treatments include various soft tissue techniques, Strand Technique, Kinesiotaping, Ultrasound among others. Book an appointment now.</p>
  <div class="card-photo" role="img" aria-label="Photo of a chiropractor adjusting a patient's back" style="height:62px;background:linear-gradient(90deg,#c9a58c,#e9d2c0 50%,#7f6a5c)"></div>
</article>

<div class="abs service-title" style="left:315px;top:671px">OSTEOPATHIC MEDICINE</div>
<article class="abs card" style="left:291px;top:695px;height:221px">
  <p>Osteopathic Medicine offers hands-on diagnosis and treatment through a system of therapy known as osteopathic manipulative medicine which emphasizes to promote the body's innate ability to heal itself. Many of osteopathic techniques are aimed at reducing or eliminating the impediments to proper structure and function so the self-healing mechanism of our bodies can assume its role in restoring a person to health.</p>
  <div class="card-photo" role="img" aria-label="Photo of hands performing osteopathic treatment" style="height:110px;background:linear-gradient(180deg,rgba(111,188,203,0),#5c6e73 40%,#2f3436)"></div>
</article>

<div class="abs service-title" style="left:563px;top:671px">FAMILY COUNSELLING</div>
<article class="abs card" style="left:539px;top:695px;height:221px">
  <p>Our relationships with ourselves and our loved ones is an integrated part of our overall well being and can often influence our bodies physically. Our registered Social Work practitioner assists clients in handling individual, family, emotional or educational issues in a professional and confidential manner. Whether it is marital issues, parenting concerns or individual matters, a chat with our counsellor can ease your stress and put you on the right path.</p>
  <div class="card-photo" role="img" aria-label="Photo of a senior couple talking with a counsellor" style="height:100px;background:linear-gradient(90deg,#dfe7ea,#c8a690 45%,#e5ecef 70%,#9fb6c2)"></div>
</article>

<!-- row 2 -->
<div class="abs service-title" style="left:67px;top:926px">MASSAGE THERAPY</div>
<article class="abs card" style="left:43px;top:950px;height:217px">
  <p>Massage Therapy is a mostly widely known for its relaxation and stress release abilities, and it is also recognized as an effective treatment for treating illness and as a tool in preventative medicine. Safe and effective massage treatments need to be carried out by registered massage therapists. Benefits of therapeutic massages include:</p>
  <ul><li>Treatment and elimination of chronic pain and acute conditions</li><li>Relaxation and release stress</li><li>Improve circulation</li><li>Improve mobility and balance</li><li>Improve the functioning of immune system</li><li>Lymphatic drainage</li></ul>
  <p style="padding-top:0">Whether you are looking to get rid of that sore back or looking for improve your golf swing, therapeutic massages can help. Book an appointment now.</p>
  <div class="card-photo" role="img" aria-label="Photo of hands massaging a back" style="height:48px;background:linear-gradient(90deg,#c79a83,#e6c4b0 50%,#b98a73)"></div>
</article>

<div class="abs service-title" style="left:315px;top:926px">PHYSIOTHERAPY</div>
<article class="abs card" style="left:291px;top:950px;height:217px">
  <p>Physiotherapy is most well known for its ability to speed up the body's recovery process from injury, illness or simple wear and tear. Whether you are looking to get better from an injury or improve your body's functionality, our physiotherapy treatments can get you back doing the things you love to do in improved performance. Some common treatments include ultrasound, manual therapy, electrical stimulation, physio-taping amongst others.</p>
  <div class="card-photo" role="img" aria-label="Photo of a physiotherapist treating a patient's leg" style="height:90px;background:linear-gradient(90deg,#d9c3b5,#b88f7a 50%,#e8dcd3)"></div>
</article>

<div class="abs service-title" style="left:563px;top:926px">ACUPUNCTURE</div>
<article class="abs card" style="left:539px;top:950px;height:217px">
  <p>Acupuncture is an ancient Chinese methodology that has been proven to be very effective in many health issues, particularly in relieving pain. It involves the stimulation of acupuncture points on the body to regain the natural balance of the body. Medical Acupuncture is effective in treating a wide variety of conditions including: headaches, neck and back pains, carpal tunnel syndrome, fibromyalgia, asthma, allergies, sinus problems, digestive disorders and many others.</p>
  <div class="card-photo" role="img" aria-label="Photo of acupuncture needles placed on a back" style="height:90px;background:linear-gradient(90deg,#c69c86,#e9cbb9 50%,#b3897a)"></div>
</article>

</body>
</html>
```